Post it Note design

POST-IT NOTE DESIGN (CONTENT)
Size recommended: 4x6 for handwriting space.
Header (Bold):
Lighting Issue Detected on Your Property
Sub-header:
During our routine night inspection, we noted the following item(s):
Checkbox List:
⬜ Building Lights Out
⬜ Pole Lights Out
⬜ Sign Not Illuminated
⬜ Other ________________________
Action Line:
We can provide a quote or dispatch service right away.
Area for notes
Contact Block (Bold & Centered):
Brovane Fixture Inc.
Service@BrovaneFixture.com
www.BrovaneFixture.com
877-514-0862
Industry/Entity Type
Electrical lighting
Colors
Designer to choose colors to be used in the design.
Look and feel
Each slider illustrates characteristics of the customer's brand and the style your logo design should communicate.

```html
<!DOCTYPE html>
<html lang="en">
<head>
<meta charset="utf-8">
<title>Lighting Issue Notice – Brovane Fixture Inc.</title>
<link href="https://fonts.googleapis.com/css2?family=Poppins:wght@500;600;700;800&display=swap" rel="stylesheet">
<style>
  :root {
    --page-bg: #e9eaec;
    --brand-blue: #2b3990;
    --brand-navy: #2e3192;
    --deep-red: #9b1b20;
    --bright-red: #ed1c24;
    --white: #ffffff;
    --sky-top: #6f98cc;
    --sky-mid: #3e5f8c;
    --night: #0f1724;
  }
  * { margin: 0; padding: 0; box-sizing: border-box; }
  html, body {
    width: 1200px; height: 2866px; overflow: hidden;
    background: var(--page-bg);
    font-family: "Poppins", sans-serif;
  }
  .notice {
    position: absolute; left: 30px; top: 664px;
    width: 1140px; height: 1538px;
    background: var(--white); overflow: hidden;
  }
  .hero {
    position: absolute; left: 0; top: 0; width: 1140px; height: 641px;
    background: linear-gradient(180deg, var(--sky-top) 0%, #7a8fa6 35%, var(--sky-mid) 60%, var(--night) 100%);
  }
  .hero-divider {
    position: absolute; left: 0; top: 641px; width: 1140px; height: 9px; background: var(--white);
  }
  .brand-name {
    position: absolute; left: 50px; top: 40px;
    display: flex; align-items: center; gap: 14px;
    color: var(--white); font-weight: 800; font-size: 34px; letter-spacing: 0.5px;
  }
  .brand-name .mark { width: 26px; height: 26px; background: var(--bright-red); }
  .headline {
    position: absolute; left: 129px; top: 375px; width: 768px; height: 140px;
    background: rgba(43, 57, 144, 0.92);
    color: var(--white); font-weight: 800; font-size: 56px; line-height: 66px;
    text-align: center; padding-top: 4px; letter-spacing: -0.5px;
  }
  .subhead {
    position: absolute; left: 0; top: 540px; width: 1140px;
    color: var(--white); font-weight: 700; font-size: 28px; line-height: 42px;
    text-align: center;
  }
  .checklist-panel {
    position: absolute; left: 0; top: 650px; width: 577px; height: 497px; background: var(--deep-red);
  }
  .notes-panel {
    position: absolute; left: 577px; top: 650px; width: 563px; height: 577px; background: var(--bright-red);
  }
  .section-title {
    position: absolute; color: var(--white); font-weight: 800; font-size: 30px;
    text-decoration: underline; text-underline-offset: 5px;
  }
  .checklist-title { left: 42px; top: 48px; }
  .notes-title { left: 28px; top: 44px; }
  .checklist { position: absolute; left: 44px; top: 108px; list-style: none; }
  .checklist li {
    display: flex; align-items: center; gap: 12px; height: 75px;
    color: var(--white); font-weight: 600; font-size: 33px;
  }
  .checklist .box { width: 18px; height: 22px; border: 2px solid var(--white); flex: none; }
  .checklist .blank {
    display: inline-block; width: 260px; height: 3px; margin: 22px 0 0 6px;
    background: repeating-linear-gradient(90deg, var(--white) 0 14px, transparent 14px 22px);
  }
  .note-line { position: absolute; left: 28px; width: 393px; height: 2px; background: var(--white); }
  .action-band {
    position: absolute; left: 0; top: 1147px; width: 597px; height: 160px;
    background: var(--brand-blue);
  }
  .action-text {
    position: absolute; left: 42px; top: 1163px; z-index: 3;
    color: var(--white); font-weight: 800; font-size: 34px; line-height: 43px;
    text-transform: uppercase;
  }
  .bucket-truck {
    position: absolute; left: 612px; top: 1035px; width: 372px; height: 259px; z-index: 2;
    border-radius: 14px;
    background: linear-gradient(180deg, #f4f4f4 0%, #dcdfe2 65%, #3a3a3a 100%);
  }
  .service-van {
    position: absolute; left: 152px; top: 1319px; width: 297px; height: 208px;
    border-radius: 14px;
    background: linear-gradient(180deg, #f7f7f7 0%, #e2e4e7 70%, #4a4a4a 100%);
  }
  .contact {
    position: absolute; left: 480px; top: 1338px; width: 540px;
    text-align: center; font-weight: 600; color: var(--brand-navy); font-style: normal;
  }
  .contact .company { color: var(--deep-red); font-weight: 800; font-size: 25px; line-height: 44px; }
  .contact .line { font-size: 26px; line-height: 42px; }
  .contact .phone { color: var(--bright-red); font-weight: 800; font-size: 36px; line-height: 56px; }
</style>
</head>
<body>
  <main class="notice">
    <section class="hero" role="img" aria-label="Photograph of large round outdoor floodlight fixtures against a blue evening sky"></section>
    <div class="hero-divider"></div>

    <div class="brand-name"><span class="mark"></span>Brovane Fixture Inc.</div>

    <h1 class="headline">LIGHTING ISSUE DETECTED<br>ON YOUR PROPERTY</h1>
    <p class="subhead">DURING OUR ROUTINE NIGHT INSPECTION,<br>WE NOTED THE FOLLOWING ITEM(S):</p>

    <section class="checklist-panel">
      <h2 class="section-title checklist-title">CHECKBOX LIST:</h2>
      <ul class="checklist">
        <li><span class="box"></span>Building Lights Out</li>
        <li><span class="box"></span>Pole Lights Out</li>
        <li><span class="box"></span>Sign Not Illuminated</li>
        <li><span class="box"></span>Other<span class="blank"></span></li>
      </ul>
    </section>

    <section class="notes-panel">
      <h2 class="section-title notes-title">AREA FOR NOTES</h2>
      <div class="note-line" style="top:140px"></div>
      <div class="note-line" style="top:204px"></div>
      <div class="note-line" style="top:267px"></div>
      <div class="note-line" style="top:332px"></div>
    </section>

    <div class="action-band"></div>
    <p class="action-text">We can provide a quote<br>or dispatch service<br>right away.</p>

    <div class="bucket-truck" role="img" aria-label="Photograph of a white bucket truck with traffic cones"></div>
    <div class="service-van" role="img" aria-label="Photograph of a white company service van"></div>

    <address class="contact">
      <div class="company">BROVANE FIXTURE INC.</div>
      <div class="line">Service@BrovaneFixture.com</div>
      <div class="line">www.BrovaneFixture.com</div>
      <div class="phone">877-514-0862</div>
    </address>
  </main>
</body>
</html>
```